Brim-Vane PowerPoint Layout Design - Updated

We're now looking for a PowerPoint Layout design for Brim-Vane. Brim-Vane is an innovative, forward thinking insurance technology designed to help Commercially Focused Insurance Brokers and Agents track their organization's strategic performance and all of the individual opportunities that they come in contact with throughout a calendar year. Users gain powerful insights for improvement, efficiencies, and effectiveness that can be shared with their insurance carrier trading partners which, in turn, benefits their clients and the insurance professionals within these same organizations.

```html
<!DOCTYPE html>
<html lang="en">
<head>
<meta charset="utf-8">
<title>Brim-Vane Presentation Layout</title>
<link href="https://fonts.googleapis.com/css2?family=Montserrat:wght@500;600;700;800&family=Poppins:wght@300;400;500&family=Oswald:wght@500;600&display=swap" rel="stylesheet">
<style>
:root{
  --green:#5c9642;
  --green-dark:#4f8a3a;
  --olive:#b9b64a;
  --gold:#e2b53a;
  --gold-badge:#e8a913;
  --cream:#f4ead0;
  --navy:#1d2438;
  --page:#f2f2f2;
  --soft:#f4f5ee;
  --text:#3a3a3a;
  --white:#ffffff;
}
*{margin:0;padding:0;box-sizing:border-box}
html,body{width:1200px;height:3652px;overflow:hidden;background:var(--page)}
body{position:relative;font-family:"Poppins",sans-serif;color:var(--text)}
.slide{position:absolute;left:99px;width:1002px;height:563px;overflow:hidden}
.slide svg.bg{position:absolute;left:0;top:0;width:1002px;height:563px}
.abs{position:absolute}
.photo{position:absolute}
.brand-foot{position:absolute;left:33px;top:523px;display:flex;align-items:center;gap:8px;font-family:"Montserrat",sans-serif;font-weight:700;font-size:22px;color:var(--green);letter-spacing:.5px}
.brand-foot .dot{width:18px;height:18px;background:var(--gold)}
.brand-foot.light{color:var(--white)}
.brand-foot.light .dot{background:var(--white)}
.page-num{position:absolute;left:959px;top:522px;width:28px;height:28px;border-radius:50%;background:var(--gold-badge);color:var(--white);font-size:13px;font-weight:500;display:flex;align-items:center;justify-content:center}
.accent-bar{position:absolute;height:4px;width:77px;background:var(--gold)}
.heading{font-family:"Montserrat",sans-serif;font-weight:700;color:var(--navy)}

/* slide 1 */
.s1{top:57px;background:var(--green)}
.s1 .brand{right:21px;top:44px;display:flex;align-items:center;gap:16px;font-family:"Montserrat",sans-serif;font-weight:800;font-size:58px;color:var(--white);line-height:1}
.s1 .brand .dot{width:40px;height:40px;background:var(--white)}
.s1 .title{right:21px;top:184px;text-align:right;font-family:"Montserrat",sans-serif;font-weight:800;font-size:44px;line-height:48px;color:var(--white)}
.s1 .lede{right:21px;top:291px;text-align:right;font-size:18px;line-height:27px;color:var(--white);font-weight:300}

/* slide 2 */
.s2{top:648px;background:var(--white)}
.toc-title{left:31px;top:50px;font-size:39px}
.toc-item{position:absolute;left:31px;width:450px;height:56px}
.toc-check{position:absolute;left:0;top:0;width:55px;height:55px;background:var(--green)}
.toc-head{position:absolute;left:71px;top:4px;font-family:"Montserrat",sans-serif;font-weight:700;font-size:15.5px;color:var(--navy)}
.toc-desc{position:absolute;left:71px;top:26px;font-size:12px;line-height:18px;color:#555}
.toc-num{position:absolute;left:410px;top:10px;width:30px;height:30px;border:1.5px solid var(--green);border-radius:50%;color:var(--green);font-size:14px;display:flex;align-items:center;justify-content:center}

/* slide 3 */
.s3{top:1244px;background:var(--soft)}
.about-title{left:0;width:1002px;top:45px;text-align:center;font-size:40px}
.about-title span{color:var(--green)}
.body-copy{font-size:12.2px;line-height:21.3px;color:#333}

/* slide 4 */
.s4{top:1838px;background:linear-gradient(100deg,#bdb84a 0%,#a6ad45 45%,#5d9743 100%)}
.divider-title{left:0;width:1002px;top:210px;text-align:center;font-family:"Montserrat",sans-serif;font-weight:700;font-size:40px;color:var(--white)}
.divider-copy{left:50px;width:902px;top:265px;text-align:center;font-size:21px;line-height:31px;color:var(--white);font-weight:300;letter-spacing:.5px}

/* slide 5 */
.s5{top:2438px;background:var(--white)}
.team-title{left:0;width:1002px;top:48px;text-align:center;font-size:44px;color:#1f1f1f}
.team-intro{left:60px;width:882px;top:108px;text-align:center;font-size:13.3px;line-height:21px;color:#333}
.card{position:absolute;top:176px;width:299px;height:315px}
.card svg{position:absolute;left:0;top:0;width:299px;height:315px}
.card .avatar{position:absolute;left:77px;top:7px;width:144px;height:144px;border-radius:50%;border:3px solid var(--white);background:linear-gradient(160deg,#c9ccd2,#5b6372)}
.card .name{position:absolute;left:0;width:299px;top:184px;text-align:center;font-family:"Oswald",sans-serif;font-weight:500;font-size:22px;color:var(--white);letter-spacing:.5px}
.card .bio{position:absolute;left:30px;width:239px;top:222px;text-align:center;font-size:11.6px;line-height:18.5px;color:var(--white)}

/* slide 6 */
.s6{top:3035px;background:linear-gradient(110deg,#c3b94a 0%,#8fad45 50%,#5d9743 100%)}
.thanks{left:539px;top:72px;font-family:"Montserrat",sans-serif;font-weight:800;font-size:46px;color:var(--white)}
.thanks-copy{left:539px;top:140px;width:440px;font-size:17px;line-height:28.5px;color:var(--white);font-weight:300}
.contact{position:absolute;left:539px;display:flex;align-items:center;gap:16px;color:var(--white);font-size:17px;line-height:25px;font-weight:300}
.contact .ring{width:62px;height:62px;border:2.5px solid var(--white);border-radius:50%;display:flex;align-items:center;justify-content:center;flex:none}
</style>
</head>
<body>

<!-- Title slide -->
<section class="slide s1">
  <svg class="bg" viewBox="0 0 706 397" preserveAspectRatio="none">
    <defs>
      <linearGradient id="meetingTone" x1="0" y1="0" x2="1" y2="1">
        <stop offset="0" stop-color="#d9cfa9"/>
        <stop offset=".5" stop-color="#a99f84"/>
        <stop offset="1" stop-color="#e6e4dc"/>
      </linearGradient>
    </defs>
    <rect width="706" height="397" fill="url(#meetingTone)" role="img" aria-label="Photo of three colleagues discussing work around a laptop"/>
    <polygon points="0,0 60,0 300,397 0,397" fill="#e2bd45" opacity=".82"/>
    <polygon points="60,0 706,0 706,397 660,397 300,180" fill="#5c9642" opacity=".9"/>
    <polygon points="60,0 150,0 300,180 300,397" fill="#ffffff" opacity=".12"/>
  </svg>
  <div class="abs brand"><span class="dot"></span>Brim-Vane</div>
  <h1 class="abs title">PRESENTATION<br>TITLE GOES HERE</h1>
  <p class="abs lede">Sed ut perspiciatis unde omnis iste natus<br>error sit voluptatem accusantium<br>doloremque enim ipsam</p>
</section>

<!-- Table of content -->
<section class="slide s2">
  <svg class="bg" viewBox="0 0 706 397" preserveAspectRatio="none">
    <polygon points="343,40 706,40 706,330 640,397 343,397" fill="#f4ead0"/>
    <polygon points="540,397 706,397 706,300" fill="#ffffff"/>
    <polygon points="295,0 706,0 706,232" fill="#5c9642"/>
  </svg>
  <div class="photo" style="left:500px;top:61px;width:486px;height:433px;background:linear-gradient(135deg,#c9ccc7,#8b7f6f 55%,#d8d6cf)" role="img" aria-label="Photo of a smiling businessman in a meeting with a laptop"></div>
  <div class="accent-bar" style="left:31px;top:35px"></div>
  <h2 class="abs heading toc-title">TABLE OF CONTENT</h2>

  <div class="toc-item" style="top:146px">
    <div class="toc-check"><svg width="55" height="55" viewBox="0 0 55 55"><polyline points="15,28 24,37 41,19" fill="none" stroke="#fff" stroke-width="6" stroke-linecap="round" stroke-linejoin="round"/></svg></div>
    <div class="toc-head">EXCEPTEUR SINT OCCAECAT</div>
    <div class="toc-desc">Nemo enim ipsam voluptatem quia voluptas sit<br>aut oditaut fugit, sed quia</div>
    <div class="toc-num">1</div>
  </div>
  <div class="toc-item" style="top:227px">
    <div class="toc-check"><svg width="55" height="55" viewBox="0 0 55 55"><polyline points="15,28 24,37 41,19" fill="none" stroke="#fff" stroke-width="6" stroke-linecap="round" stroke-linejoin="round"/></svg></div>
    <div class="toc-head">EXCEPTEUR SINT OCCAECAT</div>
    <div class="toc-desc">Nemo enim ipsam voluptatem quia voluptas sit<br>aut oditaut fugit, sed quia</div>
    <div class="toc-num">2</div>
  </div>
  <div class="toc-item" style="top:309px">
    <div class="toc-check"><svg width="55" height="55" viewBox="0 0 55 55"><polyline points="15,28 24,37 41,19" fill="none" stroke="#fff" stroke-width="6" stroke-linecap="round" stroke-linejoin="round"/></svg></div>
    <div class="toc-head">EXCEPTEUR SINT OCCAECAT</div>
    <div class="toc-desc">Nemo enim ipsam voluptatem quia voluptas sit<br>aut oditaut fugit, sed quia</div>
    <div class="toc-num">3</div>
  </div>
  <div class="toc-item" style="top:393px">
    <div class="toc-check"><svg width="55" height="55" viewBox="0 0 55 55"><polyline points="15,28 24,37 41,19" fill="none" stroke="#fff" stroke-width="6" stroke-linecap="round" stroke-linejoin="round"/></svg></div>
    <div class="toc-head">EXCEPTEUR SINT OCCAECAT</div>
    <div class="toc-desc">Nemo enim ipsam voluptatem quia voluptas sit<br>aut oditaut fugit, sed quia</div>
    <div class="toc-num">4</div>
  </div>

  <div class="brand-foot"><span class="dot"></span>BRIM-VANE</div>
  <div class="page-num">2</div>
</section>

<!-- About -->
<section class="slide s3">
  <svg class="bg" viewBox="0 0 706 397" preserveAspectRatio="none">
    <polygon points="0,0 60,0 290,397 0,397" fill="#ffffff" opacity=".7"/>
    <polygon points="0,0 30,0 0,40" fill="#ffffff"/>
    <polygon points="500,397 706,260 706,397" fill="#ffffff" opacity=".8"/>
  </svg>
  <div class="accent-bar" style="left:462px;top:33px"></div>
  <h2 class="abs heading about-title">ABOUT <span>BRIM-VANE</span></h2>
  <p class="abs body-copy" style="left:31px;top:110px;width:460px">Sed ut perspiciatis unde omnis iste natus error sit voluptatem accusantium doloremque laudantium, totam rem aperiam, eaque ipsa quae ab illo inventore veritatis et quasi architecto beatae vitae dicta sunt explicabo. Nemo enim ipsam voluptatem quia voluptas sit aspernatur aut odit aut fugit, sed quia consequuntur magni dolores eos qui ratione voluptatem sequi nesciunt. Neque porro quisquam est, qui dolorem ipsum quia dolor sit amet, consectetur.</p>
  <div class="photo" style="left:31px;top:274px;width:454px;height:232px;background:linear-gradient(135deg,#3b4a5e,#8c8377 50%,#24324a)" role="img" aria-label="Photo of four colleagues smiling around a laptop in an office"></div>
  <div class="photo" style="left:523px;top:115px;width:454px;height:232px;background:linear-gradient(120deg,#4d8aa5,#2c4f7a 55%,#7db0c4)" role="img" aria-label="Photo of a hand touching a screen with insurance service buttons"></div>
  <p class="abs body-copy" style="left:523px;top:357px;width:460px">Sed ut perspiciatis unde omnis iste natus error sit voluptatem accusantium doloremque laudantium, totam rem aperiam, eaque ipsa quae ab illo inventore veritatis et quasi architecto beatae vitae dicta sunt explicabo. Nemo enim ipsam voluptatem quia voluptas sit aspernatur aut odit aut fugit, sed quia consequuntur magni dolores eos qui ratione voluptatem sequi nesciunt. Neque porro quisquam est, qui dolorem ipsum quia dolor sit amet, consectetur.</p>
  <div class="brand-foot"><span class="dot"></span>BRIM-VANE</div>
  <div class="page-num">3</div>
</section>

<!-- Section divider -->
<section class="slide s4" role="img" aria-label="Tinted photo of hands working on a laptop with checklist documents">
  <div class="accent-bar" style="left:462px;top:197px"></div>
  <h2 class="abs divider-title">EXCEPTEUR SINT OCCAECAT CUPIDATAT</h2>
  <p class="abs divider-copy">Sed ut perspiciatis unde omnis iste natus error sit voluptatem accusantium doloremque laudantium, totam rem aperiam, eaque ipsa quae ab illo inventore veritatis et quasi.</p>
  <div class="brand-foot light"><span class="dot"></span>BRIM-VANE</div>
  <div class="page-num">4</div>
</section>

<!-- Team -->
<section class="slide s5">
  <div class="accent-bar" style="left:462px;top:37px"></div>
  <h2 class="abs heading team-title">MEET OUR TEAM</h2>
  <p class="abs team-intro">Nemo enim ipsam voluptatem quia voluptas sit aspernatur aut odit aut fugit, sed quia consequuntur magni dolores eos qui ratione voluptatem sequi nesciunt. Neque porro quisquam est, qui dolorem ipsum quia dolor sit amet,.</p>

  <div class="card" style="left:33px">
    <svg viewBox="0 0 299 315"><polygon points="0,130 299,0 299,315 0,315" fill="#5c9642"/></svg>
    <div class="avatar" role="img" aria-label="Portrait photo of a team member"></div>
    <div class="name">NAME HEADING</div>
    <div class="bio">Nemo enim ipsam voluptatem quia voluptas sit aspernatur aut odit aut fugit, sed quia consequuntur magni dolores eos qui ratione voluptatem.</div>
  </div>
  <div class="card" style="left:352px">
    <svg viewBox="0 0 299 315"><polygon points="0,130 299,0 299,315 0,315" fill="#5c9642"/></svg>
    <div class="avatar" role="img" aria-label="Portrait photo of a team member"></div>
    <div class="name">NAME HEADING</div>
    <div class="bio">Nemo enim ipsam voluptatem quia voluptas sit aspernatur aut odit aut fugit, sed quia consequuntur magni dolores eos qui ratione voluptatem.</div>
  </div>
  <div class="card" style="left:670px">
    <svg viewBox="0 0 299 315"><polygon points="0,130 299,0 299,315 0,315" fill="#5c9642"/></svg>
    <div class="avatar" role="img" aria-label="Portrait photo of a team member"></div>
    <div class="name">NAME HEADING</div>
    <div class="bio">Nemo enim ipsam voluptatem quia voluptas sit aspernatur aut odit aut fugit, sed quia consequuntur magni dolores eos qui ratione voluptatem.</div>
  </div>

  <div class="brand-foot"><span class="dot"></span>BRIM-VANE</div>
  <div class="page-num">5</div>
</section>

<!-- Thank you -->
<section class="slide s6">
  <div class="photo" style="left:13px;top:35px;width:495px;height:493px;background:linear-gradient(120deg,#2e4a78,#7c8a9c 55%,#d9dde2)" role="img" aria-label="Photo of a smiling businessman shaking hands"></div>
  <svg class="bg" viewBox="0 0 706 397" preserveAspectRatio="none">
    <polygon points="9,25 358,330 358,397 185,397" fill="#c4b94a"/>
  </svg>
  <h2 class="abs thanks">THANK YOU!</h2>
  <p class="abs thanks-copy">Neque porro quisquam est, qui dolorem ipsum quia dolor sit amet, consectetur, adipisci velit, sed quia non numquam eius.</p>
  <div class="contact" style="top:246px">
    <span class="ring"><svg width="24" height="24" viewBox="0 0 24 24"><path d="M12 2a7 7 0 0 0-7 7c0 5 7 13 7 13s7-8 7-13a7 7 0 0 0-7-7zm0 9.5A2.5 2.5 0 1 1 12 6.5a2.5 2.5 0 0 1 0 5z" fill="#fff"/></svg></span>
    <span>Nemo enim ipsam<br>volu ptatem quia voluptas</span>
  </div>
  <div class="contact" style="top:332px">
    <span class="ring"><svg width="22" height="22" viewBox="0 0 24 24"><path d="M6.6 10.8a15 15 0 0 0 6.6 6.6l2.2-2.2a1 1 0 0 1 1-.25 11.4 11.4 0 0 0 3.6.57 1 1 0 0 1 1 1V20a1 1 0 0 1-1 1A17 17 0 0 1 3 4a1 1 0 0 1 1-1h3.5a1 1 0 0 1 1 1c0 1.25.2 2.45.57 3.57a1 1 0 0 1-.25 1z" fill="#fff"/></svg></span>
    <span>1-800-555-0142</span>
  </div>
  <div class="contact" style="top:431px">
    <span class="ring"><svg width="22" height="22" viewBox="0 0 24 24"><path d="M3 5h18v14H3z" fill="#fff"/><path d="M3 5l9 7 9-7" fill="none" stroke="#8fad45" stroke-width="1.6"/></svg></span>
    <span>info@brimvane.com</span>
  </div>
</section>

</body>
</html>
```